Design some Business Cards for wedding photographers

My sister and I are wedding photographers. Our company is called FERN Wedding Photography. We need some business cards. Here is the information that needs to be on our card:

FERN Wedding Photography

fernwedphoto@[login to view URL]
(424) 555-0198

We are going to use the same design for both of us but we would also like to have personalized cards. They can look the same but also have our names on it which are (we need individual cards obviously):

Mira Castell
Dorota Brandt

I am attaching our logo design. I also like the black background, it's also attached but we are open for different backgrounds as well.

Business cards should be two sided (the front and the back) and be standard size 3.5 x 2 in.

We would also like some sort of a sparkly effect on the ring.

I attached all the versions of the logo. You don't need all of them, you can just download the most appropriate format for you. The last two files is background.

```html
<!DOCTYPE html>
<html lang="en">
<head>
<meta charset="utf-8">
<title>FERN Wedding Photography – Business Cards</title>
<link rel="stylesheet" href="https://fonts.googleapis.com/css2?family=Raleway:wght@300;400&display=swap">
<style>
  :root {
    --backdrop: #3a3a3c;
    --card: #232324;
    --mint: #cfe8d2;
    --gold: #c9a56a;
    --muted: #a9a9a9;
    --text-light: #e6e6e6;
    --rule: #d8d8d8;
  }
  * { margin: 0; padding: 0; box-sizing: border-box; }
  html, body {
    width: 1200px;
    height: 799px;
    overflow: hidden;
    background: var(--backdrop);
    font-family: "Raleway", "Helvetica Neue", Arial, sans-serif;
  }
  .sheet {
    width: 1200px;
    height: 799px;
    display: flex;
    align-items: center;
    justify-content: center;
    gap: 44px;
  }
  .card {
    position: relative;
    width: 525px;
    height: 300px;
    background: var(--card);
    box-shadow: 0 10px 30px rgba(0,0,0,0.35);
  }

  /* Front: brand */
  .card--front {
    display: flex;
    align-items: center;
    justify-content: center;
  }
  .brand {
    display: flex;
    align-items: center;
    gap: 14px;
  }
  .brand__mark {
    width: 18px;
    height: 18px;
    border-radius: 50%;
    background: var(--gold);
  }
  .brand__name {
    color: var(--gold);
    font-weight: 400;
    font-size: 30px;
    line-height: 1.15;
    letter-spacing: 0.5px;
    text-align: center;
  }

  /* Back: contact */
  .card--back { padding: 38px 40px; color: var(--text-light); }
  .person__name {
    font-size: 22px;
    font-weight: 400;
    letter-spacing: 1px;
    text-transform: uppercase;
    color: var(--mint);
  }
  .person__role {
    display: flex;
    align-items: center;
    gap: 10px;
    margin-top: 4px;
    font-size: 13px;
    font-weight: 300;
    color: var(--muted);
  }
  .person__rule {
    flex: 1;
    height: 1px;
    background: var(--rule);
    margin-top: 10px;
  }
  .contact {
    list-style: none;
    margin-top: 18px;
    text-align: right;
    font-size: 14px;
    font-weight: 300;
    line-height: 1.45;
    color: var(--text-light);
  }
</style>
</head>
<body>
  <main class="sheet">
    <section class="card card--front" aria-label="Card front">
      <div class="brand">
        <span class="brand__mark" aria-hidden="true"></span>
        <p class="brand__name">FERN<br>wedding photography</p>
      </div>
    </section>

    <section class="card card--back" aria-label="Card back">
      <h1 class="person__name">Dorota Brandt</h1>
      <div class="person__role">
        <span>Wedding Photographer</span>
        <span class="person__rule" aria-hidden="true"></span>
      </div>
      <ul class="contact">
        <li>(424) 555-0198</li>
        <li>fernwedphoto@fernmail.com</li>
        <li>social.fernwedphoto.com</li>
        <li>fernwedphoto.com</li>
      </ul>
    </section>
  </main>
</body>
</html>
```